Postcard Design

My company name is Lumen Aerial. We offer FAA approved drone photography and videography for real estate marketing. Our target demographic customer base is Realtors, Real Estate Brokerages (their Brokers in Charge "BIC's and owners), Builders and Developers. There are currently only two FAA approved drone operators in the greater Raleigh "Triangle" area. Our website is www.LumenAerialfly.example. All current packages and pricing are featured there. Our prices are extremely affordable by design to make drone marketing available to all types of real estate rather than just the luxury markets. I have a Lumen Crescent logo for our real estate business but I'd like to modify it a bit to replace "Realty Greoup" with "Aerial" and have an image of a Skyvane Kestrel IV underneath Lumen (black with the same effect as the word "Triangle". I'll provide examples of my photography as well as the logo I'd like modified. I'd like this post card to be eye catching and include a 25% off promotion off all our packages through January, 2016. The postcard can be two sided. Our motto is "Let Lumen Aerial lift your real estate marketing above the rest". I prefer a clean contemporary feel rather than the cartoonish cluttered look.

Industry/Entity Type

Real Estate

```html
<!DOCTYPE html>
<html lang="en">
<head>
<meta charset="utf-8">
<title>Lumen Aerial Postcard</title>
<link href="https://fonts.googleapis.com/css2?family=Roboto+Condensed:wght@400;700&family=Roboto:wght@400;500&display=swap" rel="stylesheet">
<style>
  :root {
    --page: #e9eaeb;
    --white: #ffffff;
    --ink: #2a2a2a;
    --blue: #2a7799;
    --blue-dark: #1f5f7d;
    --orange: #e8885a;
    --steel: #9fb5c2;
    --pale: #eef1f3;
    --price-box: #e7eaec;
    --muted: #8a8f93;
    --line: #d6dadd;
    --body-text: #444444;
  }
  * { box-sizing: border-box; margin: 0; padding: 0; }
  html, body { width: 900px; height: 1200px; overflow: hidden; }
  body { background: var(--page); font-family: "Roboto Condensed", "Arial Narrow", sans-serif; color: var(--ink); position: relative; }

  .card { position: absolute; left: 60px; width: 780px; background: var(--white); box-shadow: 0 3px 10px rgba(0,0,0,.18); overflow: hidden; }
  .card--front { top: 40px; height: 500px; background: var(--pale); }
  .card--back { top: 640px; height: 500px; }

  .brand { position: absolute; font-family: "Roboto Condensed", sans-serif; font-weight: 700; color: var(--ink); font-size: 40px; letter-spacing: -0.5px; line-height: 1; white-space: nowrap; }
  .brand__mark { display: inline-block; width: 14px; height: 14px; background: var(--orange); margin-right: 8px; vertical-align: 6px; }

  /* Front */
  .front__top { position: absolute; left: 0; top: 0; width: 780px; height: 140px; background: var(--pale); }
  .front__top .brand { left: 28px; top: 62px; }
  .promo-tag { position: absolute; left: 300px; top: 30px; width: 460px; height: 86px; }
  .promo-tag svg { position: absolute; inset: 0; }
  .promo-tag__text { position: absolute; left: 72px; top: 10px; display: flex; align-items: center; gap: 10px; white-space: nowrap; }
  .promo-tag__pct { font-size: 46px; font-weight: 700; color: var(--white); letter-spacing: -1px; }
  .promo-tag__detail { color: var(--blue-dark); font-weight: 700; line-height: 1.05; }
  .promo-tag__detail b { display: block; font-size: 29px; }
  .promo-tag__detail span { display: block; font-size: 19px; }

  .price-band { position: absolute; left: 0; top: 140px; width: 780px; height: 86px; background: var(--blue); display: flex; justify-content: space-between; padding: 12px 22px 0; }
  .price { width: 160px; }
  .price__name { background: var(--white); color: var(--blue-dark); font-weight: 700; font-size: 17px; text-align: center; height: 26px; line-height: 26px; }
  .price__value { background: var(--price-box); height: 34px; display: flex; align-items: baseline; justify-content: space-between; padding: 4px 8px 0; }
  .price__old { color: var(--muted); font-size: 17px; text-decoration: line-through; }
  .price__new { color: var(--orange); font-weight: 700; font-size: 24px; }
  .price__new small { font-size: 15px; font-weight: 400; }

  .gallery { position: absolute; left: 0; top: 246px; width: 780px; height: 182px; background: var(--steel); display: flex; justify-content: space-between; align-items: center; padding: 0 22px; }
  .gallery__photo { width: 210px; height: 162px; }
  .gallery__photo--estate { background: linear-gradient(160deg, #3f6b2a, #7fae47 55%, #5a5f5a); }
  .gallery__photo--house { background: linear-gradient(180deg, #7aa6d6 0%, #4f7c3a 45%, #b9b8b0 100%); }
  .gallery__photo--lodge { width: 222px; background: linear-gradient(140deg, #3e5d2a, #8fa448 50%, #8b4a36 75%, #6c8a3b); }

  .motto { position: absolute; left: 0; top: 442px; width: 780px; height: 58px; background: var(--blue); font-weight: 700; font-size: 25px; color: var(--orange); line-height: 58px; padding-left: 18px; white-space: nowrap; }
  .motto b { color: var(--white); }

  /* Back */
  .back__head .brand { left: 36px; top: 46px; font-size: 34px; }
  .back__head .brand__mark { width: 12px; height: 12px; vertical-align: 5px; }
  .contact { position: absolute; left: 282px; top: 26px; color: var(--blue); font-weight: 700; line-height: 1.15; white-space: nowrap; }
  .contact__web { font-size: 18px; }
  .contact__phone { font-size: 30px; }
  .contact__email { font-size: 18px; }
  .stamp-box { position: absolute; right: 34px; top: 20px; width: 72px; height: 86px; border: 1px solid var(--line); }

  .intro-band { position: absolute; left: 0; top: 120px; width: 780px; height: 64px; background: var(--blue); color: var(--white); font-family: "Roboto", sans-serif; font-size: 14px; line-height: 24px; padding: 8px 28px; white-space: nowrap; }
  .intro-band strong { color: var(--orange); font-weight: 500; }

  .packages { position: absolute; left: 0; top: 184px; width: 518px; height: 236px; background: var(--pale); padding: 10px 28px; }
  .packages__title { color: var(--blue-dark); font-size: 16px; margin-bottom: 8px; }
  .packages__title b { font-size: 18px; }
  .package { display: flex; align-items: flex-start; height: 45px; }
  .package:last-child { height: auto; }
  .package__name { width: 140px; height: 26px; background: var(--orange); color: var(--white); font-weight: 700; font-size: 14px; text-align: center; line-height: 26px; flex: none; }
  .package__desc { margin-left: 18px; font-family: "Roboto Condensed", sans-serif; font-size: 10px; line-height: 1.3; color: var(--body-text); white-space: nowrap; }

  .address { position: absolute; left: 556px; width: 190px; border-top: 1px solid var(--line); }
  .address--1 { top: 266px; }
  .address--2 { top: 292px; }
  .address--3 { top: 318px; }
  .address--4 { top: 344px; }

  .license { position: absolute; left: 0; top: 420px; width: 316px; height: 80px; background: var(--steel); color: var(--white); font-family: "Roboto", sans-serif; font-size: 13px; line-height: 19px; padding: 12px 26px; }
</style>
</head>
<body>

<section class="card card--front" aria-label="Postcard front">
  <header class="front__top">
    <div class="brand"><span class="brand__mark"></span>Lumen Aerial</div>
    <div class="promo-tag">
      <svg viewBox="0 0 460 86" width="460" height="86" aria-hidden="true">
        <polygon points="0,44 42,2 456,10 450,84 42,82" fill="#e8885a"/>
        <circle cx="26" cy="44" r="4" fill="#ffffff"/>
      </svg>
      <div class="promo-tag__text">
        <span class="promo-tag__pct">25% off</span>
        <span class="promo-tag__detail"><b>all our packages</b><span>through January, 2016</span></span>
      </div>
    </div>
  </header>

  <div class="price-band">
    <div class="price"><div class="price__name">STARTER</div><div class="price__value"><span class="price__old">$99</span><span class="price__new">$74<small>,25</small></span></div></div>
    <div class="price"><div class="price__name">EXPERT</div><div class="price__value"><span class="price__old">$149</span><span class="price__new">$111<small>,75</small></span></div></div>
    <div class="price"><div class="price__name">TOP PRODUCER</div><div class="price__value"><span class="price__old">$399</span><span class="price__new">$299<small>,25</small></span></div></div>
    <div class="price"><div class="price__name">FREQUENT FLYER</div><div class="price__value"><span class="price__old">$600</span><span class="price__new">$450<small>,00</small></span></div></div>
  </div>

  <div class="gallery">
    <div class="gallery__photo gallery__photo--estate" role="img" aria-label="Aerial photo of a wooded estate with a winding driveway"></div>
    <div class="gallery__photo gallery__photo--house" role="img" aria-label="Drone photo of a suburban house with a long driveway"></div>
    <div class="gallery__photo gallery__photo--lodge" role="img" aria-label="Aerial photo of a brick lodge home on a green lawn"></div>
  </div>

  <p class="motto">Let <b>Lumen Aerial</b> lift your real estate marketing above the rest!</p>
</section>

<section class="card card--back" aria-label="Postcard back">
  <header class="back__head">
    <div class="brand"><span class="brand__mark"></span>Lumen Aerial</div>
    <div class="contact">
      <div class="contact__web">www.LumenAerialfly.example</div>
      <div class="contact__phone">555-014-2270</div>
      <div class="contact__email">AveryMoss@LumenCrescent.example</div>
    </div>
    <div class="stamp-box"></div>
  </header>

  <p class="intro-band">We offer <strong>FAA approved</strong> drone high definition photography and videography for your real estate marketing.<br>Our affordable prices make drone marketing available to all types of real estate.</p>

  <div class="packages">
    <p class="packages__title">Here are the details of our <b>packages</b>:</p>
    <div class="package"><span class="package__name">STARTER</span><p class="package__desc">10 high-resolution aerial still images<br>limited to one location</p></div>
    <div class="package"><span class="package__name">EXPERT</span><p class="package__desc">20 high-resolution aerial still images<br>limited to one location</p></div>
    <div class="package"><span class="package__name">TOP PRODUCER</span><p class="package__desc">2 minute edited high-resolution aerial video with music and branding<br>Additional narration $75 (customer to provide verbiage)</p></div>
    <div class="package"><span class="package__name">FREQUENT FLYER</span><p class="package__desc">Edited high-resolution aerial photography and videography (up to 2 minutes)<br>with music and branding<br>20 high-resolution aerial still images. (2) 10 high-resolution aerial still images<br>Can be used on multiple listings</p></div>
  </div>

  <div class="address address--1"></div>
  <div class="address address--2"></div>
  <div class="address address--3"></div>
  <div class="address address--4"></div>

  <p class="license">FAA Exemption # 20481<br>Regulatory Docket # FAA-2015-0000</p>
</section>

</body>
</html>
```